2014 Card

I need a vertical business card designed to incorporate 2 Companies in wheaton IL. First company is one o frame (I always type this with no caps and in Cataneo BT font. I like the way the L and the P surround the i) This is a Photography company that does Wedding Photography, Portraiture, Sunset, and many other types of Photography. The website is www.oneoframe-demo.com
The other company is Grand Kiosk Max a Photo Booth rental Company. We rent photo booths to weddings and all types of events. The end project should mainly appeal to Brides and show Class. I have added 2 files One is the Grand Kiosk Max Logo and the other is on one O frames header on the website. I do Like the eye in the sky on the one O frame file

Target Market(s)

Future brides

Industry/Entity Type

Business

Requirements
Must have
• Grand Kiosk Max part should say A Photo Booth Rental Company
one o frame should say All in one photography studio and address should be on this side,

```html
<!DOCTYPE html>
<html lang="en">
<head>
<meta charset="utf-8">
<title>one o frame – Business Card</title>
<link href="https://fonts.googleapis.com/css2?family=Quicksand:wght@300;400;500&display=swap" rel="stylesheet">
<style>
  :root {
    --card-bg: #ffffff;
    --ink: #1c1c1c;
    --ink-soft: #2a2a2a;
    --sky-blush: #f6d2c2;
    --sky-peach: #f0a47f;
    --sky-coral: #e99a7a;
    --cloud-mauve: #c7a3a3;
    --cloud-slate: #9a98ae;
  }
  html, body {
    margin: 0;
    padding: 0;
    width: 686px;
    height: 1200px;
    overflow: hidden;
    background: var(--card-bg);
  }
  .card {
    position: relative;
    width: 686px;
    height: 1200px;
    background: var(--card-bg);
    font-family: "Quicksand", sans-serif;
    color: var(--ink);
  }
  .brand {
    position: absolute;
    top: 98px;
    left: 0;
    width: 686px;
    margin: 0;
    text-align: center;
    font-family: "Quicksand", sans-serif;
    font-weight: 500;
    font-size: 104px;
    line-height: 1;
    letter-spacing: 1px;
    color: var(--ink);
  }
  .sunset-photo {
    position: absolute;
    top: 252px;
    left: 0;
    width: 686px;
    height: 446px;
    background: linear-gradient(180deg,
      rgba(255,255,255,1) 0%,
      var(--sky-blush) 14%,
      var(--sky-peach) 30%,
      var(--sky-coral) 45%,
      var(--cloud-mauve) 58%,
      var(--cloud-slate) 68%,
      rgba(205,204,216,0.9) 82%,
      rgba(255,255,255,1) 100%);
  }
  .tagline {
    position: absolute;
    top: 720px;
    left: 0;
    width: 686px;
    margin: 0;
    text-align: center;
    font-family: "Quicksand", sans-serif;
    font-weight: 300;
    font-style: italic;
    font-size: 46px;
    line-height: 58px;
    color: var(--ink);
  }
  .contact {
    position: absolute;
    right: 40px;
    top: 946px;
    margin: 0;
    padding: 0;
    list-style: none;
    text-align: right;
    font-family: "Quicksand", sans-serif;
    font-weight: 300;
    font-size: 38px;
    color: var(--ink-soft);
  }
  .contact li {
    line-height: 61px;
  }
</style>
</head>
<body>
  <main class="card">
    <h1 class="brand">one o frame</h1>
    <div class="sunset-photo" role="img" aria-label="Photograph of the sun setting behind soft orange and slate clouds"></div>
    <p class="tagline">All in one photography studio</p>
    <ul class="contact">
      <li class="contact-email">dana@gkmax-demo.com</li>
      <li class="contact-phone">630-555-0147</li>
      <li class="contact-web">www.oneoframe-demo.com</li>
    </ul>
  </main>
</body>
</html>
```